Webdesign für Beratung zu Themen der Qualität und Nachhaltigkeit
Zielgruppe
Ich werde mich ab 1.1.23 selbständig machen mit der Beratung zu Themen der Qualität und Nachhaltigkeit. Meine Zielgruppe sind Bildungsinstitutionen, insbesondere Volkshochschulen.
Die Webseite richtet sich an das Management von Bildungseinrichtungen.
Aufgabenstellung
Ich habe bereits eine Visitenkarte, an deren Design sich orientiert werden kann. Ich habe dieses über ein Visitenkarten-Tool erstellen lassen und besitze keine Daten dazu. Ein Foto hänge ich an.

```html
<!DOCTYPE html>
<html lang="de">
<head>
<meta charset="utf-8">
<title>Marlene Voskamp – Qualität und Nachhaltigkeit in der Bildung</title>
<link href="https://fonts.googleapis.com/css2?family=Lato:ital,wght@0,300;0,400;0,700;1,400&display=swap" rel="stylesheet">
<style>
:root{
  --dark:#34373d;
  --light:#ececec;
  --white:#ffffff;
  --ink:#111111;
  --tab-grey:#6f757d;
  --line:#d6d6d6;
  --black-btn:#17181b;
}
*{margin:0;padding:0;box-sizing:border-box}
html,body{width:1200px;height:2625px;overflow:hidden}
body{font-family:"Lato",sans-serif;color:var(--ink);background:var(--white);position:relative}
.abs{position:absolute}
.ph{position:absolute}

/* about backdrop (drawn first, hero overlaps it) */
.about-bg{left:0;top:460px;width:1200px;height:900px;background:var(--light)}
.about-photo{left:0;top:460px;width:450px;height:900px;background:linear-gradient(90deg,#c9c9c9,#dcdcdc 60%,#e6e6e6)}
.about-post{left:450px;top:460px;width:285px;height:900px;background:linear-gradient(90deg,#e4e4e4,#efefef)}

/* hero */
.hero-bg{left:0;top:0;width:1200px;height:580px}
.brand{left:153px;top:28px;color:var(--white);font-weight:700;font-size:28px;letter-spacing:-0.3px}
.nav{top:40px;right:171px;display:flex;gap:55px;color:var(--white);font-size:15px}
.hero-photo{left:760px;top:40px;width:285px;height:520px;border-radius:120px 120px 0 0;background:linear-gradient(180deg,#8a8c90,#6d7075 55%,#3a3c40);clip-path:polygon(0 0,100% 0,100% 518px,0 492px)}
.hero-title{left:146px;top:157px;color:var(--white);font-weight:300;font-size:47px;line-height:58px}
.hero-sub{left:150px;top:340px;color:#e4e4e4;font-weight:300;font-size:17px}
.call-btn{left:151px;top:388px;width:221px;height:44px;background:var(--white);border:1px solid #bbb;display:flex;align-items:center;justify-content:center;gap:12px;font-size:17px;color:#222}

/* about */
.section-title{width:1200px;left:0;text-align:center;font-weight:300;font-size:48px;color:#222}
.about-lead{left:221px;top:660px;width:760px;font-style:italic;font-size:15px;line-height:23px;text-align:justify;color:#111}
.tab{top:740px;height:38px;display:flex;align-items:center;padding:0 17px;font-size:14px}
.tab-active{left:227px;width:184px;background:var(--black-btn);color:var(--white);font-weight:700}
.tab-idle{left:422px;width:184px;background:var(--tab-grey);color:var(--white)}
.cv-card{left:218px;top:778px;width:765px;height:530px;background:var(--white);border:1px solid #ddd}
.cv-entry{position:absolute;font-size:13px;line-height:22px;color:#111}
.cv-entry b.role{display:block;font-size:15px;font-weight:700}
.cv-text{left:43px;top:108px;width:680px;font-size:13px;line-height:19.5px}
.cv-rule{position:absolute;left:33px;width:697px;height:1px;background:var(--line)}
.badge{left:273px;top:220px;width:92px;height:46px;border:1px solid #ddd;display:flex;align-items:center;justify-content:center;font-size:12px;font-weight:700}

/* services */
.services-sub{left:0;width:1200px;top:1496px;text-align:center;font-size:13px;font-weight:300;color:#222}
.services-text{left:146px;top:1543px;width:910px;font-size:13.5px;font-weight:300;line-height:22px;color:#222}
.tile{position:absolute;width:438px;height:168px;overflow:hidden}
.tile-label{position:absolute;left:0;bottom:0;width:100%;min-height:44px;background:rgba(30,32,36,.55);color:var(--white);font-weight:700;font-size:19px;text-align:center;padding:8px 10px;line-height:22px}
.tile-efqm{left:150px;top:1630px;background:linear-gradient(135deg,#e6e6e6,#f2f2f2 60%,#e9e9ec)}
.tile-quality{left:613px;top:1630px;background:radial-gradient(circle at 55% 35%,#5a6a4a,#1e2a35 70%)}
.tile-green{left:154px;top:1821px;background:radial-gradient(circle at 60% 40%,#9bcf5a,#3f8a2e 70%)}
.tile-edu{left:613px;top:1821px;background:linear-gradient(180deg,#8b8e93,#4c5058)}

/* contact */
.contact-bg{left:0;top:2070px;width:1200px;height:555px}
.contact-photo{left:0;top:2075px;width:490px;height:550px;background:linear-gradient(90deg,#6b6d72,#555860 60%,#3c3f46);clip-path:polygon(0 0,490px 45px,490px 100%,0 100%)}
.contact-title{left:518px;top:2185px;font-weight:300;font-size:48px;color:var(--white)}
.contact-item{top:2262px;display:flex;align-items:center;gap:10px;color:var(--white);font-size:13px}
.field{position:absolute;background:var(--white);height:38px;width:255px;padding:11px 18px;font-size:11px;color:#999;border:1px solid #ccc}
.send{left:793px;top:2496px;width:255px;height:39px;background:var(--black-btn);color:var(--white);font-weight:700;font-size:15px;display:flex;align-items:center;justify-content:center;gap:12px;letter-spacing:.5px}
</style>
</head>
<body>

<!-- about backdrop -->
<div class="abs about-bg"></div>
<div class="ph about-post" role="img" aria-label="Helles Holz im Hintergrund"></div>
<div class="ph about-photo" role="img" aria-label="Blasses Porträtfoto der Beraterin, lächelnd"></div>

<!-- hero -->
<svg class="abs hero-bg" viewBox="0 0 1200 580" aria-hidden="true">
  <defs><linearGradient id="heroGrad" x1="0" y1="0" x2="1" y2="1"><stop offset="0" stop-color="#2f3237"/><stop offset="1" stop-color="#4a4e56"/></linearGradient></defs>
  <polygon points="0,0 1200,0 1200,572 0,462" fill="url(#heroGrad)"/>
</svg>
<div class="ph hero-photo" role="img" aria-label="Porträtfoto der Beraterin mit verschränkten Armen"></div>
<div class="abs brand">MARLENE VOSKAMP</div>
<nav class="abs nav"><span>ÜBER MICH</span><span>MEINE LEISTUNGEN</span><span>KONTAKT</span></nav>
<h1 class="abs hero-title">EFQM,<br>Qualitätsmanagement,<br>Nachhaltigkeitsmanagement</h1>
<p class="abs hero-sub">für Volkshochschulen und andere Institutionen der Erwachsenenbildung</p>
<div class="abs call-btn">
  <svg width="20" height="20" viewBox="0 0 24 24" fill="none" stroke="#222" stroke-width="1.6"><path d="M5 3h4l2 5-2.5 1.5a11 11 0 0 0 6 6L16 13l5 2v4a2 2 0 0 1-2 2A16 16 0 0 1 3 5a2 2 0 0 1 2-2z"/></svg>
  <span>+49 151 0000 4821</span>
</div>

<!-- about -->
<h2 class="abs section-title" style="top:588px">Über mich</h2>
<p class="abs about-lead">Selbstständig, Verantwortlich Ressourcen schonen - Beratung zu Nachhaltigkeit &amp; Qualität, Marlene Voskamp - Qualität und Nachhaltigkeit in der Bildung</p>
<div class="abs tab tab-active">Professional experience</div>
<div class="abs tab tab-idle">Educational background</div>

<div class="abs cv-card">
  <div class="cv-entry" style="left:43px;top:30px"><b>Current</b> 8 months, since May 2022<b class="role">Verantwortlich Ressourcen schonen - Beratung zu Nachhaltigkeit &amp; Qualität</b>Marlene Voskamp - Qualität und Nachhaltigkeit in der Bildung</div>
  <p class="abs cv-text">Volkshochschulen und andere Bildungsinstitutionen sichern unsere Zukunft. Auch indem sie verantwortlich mit Energie und anderen Ressourcen umgehen. Ich unterstütze dabei, eine qualitätsgesicherte Nachhaltigkeit praktisch umzusetzen und damit lehrend und Beispiel gebend voranzugehen.</p>
  <div class="cv-entry" style="left:43px;top:208px">8 months, Mar 2021 - Oct 2021<b class="role">Leiterin Mehrgenerationenhaus</b>Stadt Lindenau</div>
  <div class="abs badge">Lindenau</div>
  <div class="cv-entry" style="left:458px;top:208px">10 years and 5 months, Oct 2010 - Feb 2021<b class="role">Geschäftsführerin</b>Volkshochschule Birkental e.V.</div>
  <div class="cv-rule" style="top:285px"></div>
  <div class="cv-entry" style="left:48px;top:305px">7 years and 7 months, Mar 2003 - Sep 2010<b class="role">Dozentin für Betriebswirtschaft und Marketing</b>Bildungszentrum Hollfeld</div>
  <div class="cv-entry" style="left:458px;top:305px">1 year and 9 months, Feb 2001 - Oct 2002<b class="role">Communication Managerin E-Commerce</b>Torvik AG, Vaduz, Liechtenstein</div>
  <div class="cv-rule" style="top:382px"></div>
  <div class="cv-entry" style="left:48px;top:402px">2 years and 9 months, Apr 1998 - Dec 2000<b class="role">Assistenz der Verkaufsleitung</b>BRANDEL Vertriebs GmbH</div>
  <div class="cv-entry" style="left:458px;top:402px">6 months, Oct 1997 - Mar 1998<b class="role">Assistenz der Geschäftsführung</b>BRANDEL Vertriebs GmbH</div>
</div>

<!-- services -->
<h2 class="abs section-title" style="top:1438px">Meine Leistungen</h2>
<p class="abs services-sub">Verantwortlich Ressourcen schonen - Beratung zu Nachhaltigkeit &amp; Qualität</p>
<p class="abs services-text">Volkshochschulen und andere Bildungsinstitutionen sichern unsere Zukunft. Auch indem sie verantwortlich mit Energie und anderen Ressourcen umgehen. Ich unterstütze dabei, eine qualitätsgesicherte Nachhaltigkeit praktisch umzusetzen und damit lehrend und Beispiel gebend voranzugehen.</p>

<div class="tile tile-efqm" role="img" aria-label="EFQM-Illustration mit Diagrammen vor weißer Ziegelwand"></div>
<div class="tile tile-quality" role="img" aria-label="Hand unter fünf goldenen Sternen"><div class="tile-label">Qualitätsmanagement</div></div>
<div class="tile tile-green" role="img" aria-label="Hand hält Erdkugel mit Baum und Schmetterlingen"><div class="tile-label">Nachhaltigkeitsmanagement</div></div>
<div class="tile tile-edu" role="img" aria-label="Teilnehmende in einem Seminarraum"><div class="tile-label">für Volkshochschulen und andere Institutionen der Erwachsenenbildung</div></div>

<!-- contact -->
<svg class="abs contact-bg" viewBox="0 0 1200 555" aria-hidden="true">
  <defs><linearGradient id="ctGrad" x1="0" y1="0" x2="1" y2="1"><stop offset="0" stop-color="#3a3d44"/><stop offset="1" stop-color="#555962"/></linearGradient></defs>
  <polygon points="0,5 1200,115 1200,555 0,555" fill="url(#ctGrad)"/>
</svg>
<div class="ph contact-photo" role="img" aria-label="Foto der Beraterin in Lederjacke vor einer Holzwand"></div>
<h2 class="abs contact-title">Kontakt</h2>
<div class="abs contact-item" style="left:518px">
  <svg width="16" height="16" viewBox="0 0 24 24" fill="none" stroke="#fff" stroke-width="1.6"><path d="M22 2 2 11l8 3 3 8z M10 14l12-12"/></svg>info@voskamp-beratung.de</div>
<div class="abs contact-item" style="left:721px">
  <svg width="16" height="16" viewBox="0 0 24 24" fill="none" stroke="#fff" stroke-width="1.6"><path d="M5 3h4l2 5-2.5 1.5a11 11 0 0 0 6 6L16 13l5 2v4a2 2 0 0 1-2 2A16 16 0 0 1 3 5a2 2 0 0 1 2-2z"/></svg>+49 151 0000 4821</div>
<div class="abs contact-item" style="left:906px">
  <svg width="16" height="18" viewBox="0 0 24 28" fill="#fff"><path d="M12 0a10 10 0 0 0-10 10c0 7 10 18 10 18s10-11 10-18A10 10 0 0 0 12 0zm0 14a4 4 0 1 1 0-8 4 4 0 0 1 0 8z"/></svg>Lindenau, Germany</div>
<div class="field" style="left:522px;top:2310px">Vorname</div>
<div class="field" style="left:793px;top:2310px">Nachname</div>
<div class="field" style="left:522px;top:2364px">Email</div>
<div class="field" style="left:793px;top:2364px">Telefon</div>
<div class="field" style="left:522px;top:2418px;width:526px;height:67px">Kommentare</div>
<div class="abs send">
  <svg width="16" height="16" viewBox="0 0 24 24" fill="none" stroke="#fff" stroke-width="1.6"><path d="M22 2 2 11l8 3 3 8z M10 14l12-12"/></svg>SENDEN</div>

</body>
</html>
```